Amber Meadow--logo + label design for all products sizes and type

I make hair oils and sprays. it is called Amber Meadow based on 1 Corinthians concept of a women's hair being her glory. I would like the verse to be on the labels. I need labels for 8oz and 4oz bottles, the mist and leave in conditioner use the same bottles as the oil. here is the link for what they look like
-- https://www.qorvane-jars.com/512d/lum284b.html
the conditioner is going to be in a black jar 8oz here is the link
-- https://www.qorvane-jars.com/512d/lum71q.html
I want the label to be elegant but get straight to the point of what the products are.
Although is designed for African American Hair, it can also be used Multi-Cultural so I would like it to give that vibe. thank you!!
I uploaded the pictures of the bottles.
Updates

the name of the company is Amber Meadow, not Amber Meadow Oil Added Sunday, September 11, 2016

Target Market(s)

mainly African American, but also all races

Industry/Entity Type

Hair

Requirements
Must have
• 1 Corinthians 11:15
• -elegant color, the bottles I will be using is black
• -African theme, such as (pattern, 100% natural African American hair, African continent) just something that reps Africa!!!
Nice to have
• all natural ingredients
• conditioner base is organic

```html
<!DOCTYPE html>
<html lang="en">
<head>
<meta charset="utf-8">
<title>Amber Meadow — Hair Oil Labels</title>
<link rel="stylesheet" href="https://fonts.googleapis.com/css2?family=Josefin+Sans:wght@400;600&family=Lato:wght@400;700&family=Oswald:wght@600&family=Dancing+Script&display=swap">
<style>
  :root {
    --backdrop: #e6e6e6;
    --label-black: #0c0c0c;
    --ivory: #e4e0d6;
    --muted: #a29e95;
    --verse: #8a8780;
    --amber: #d58a1f;
    --amber-deep: #c27a1e;
    --crimson: #b0182a;
    --sage: #8e9484;
    --pattern-grey: #444444;
    --kente-red: #a82a2a;
    --kente-green: #2f7a3a;
    --kente-gold: #c99a2e;
  }
  * { margin: 0; padding: 0; box-sizing: border-box; }
  html, body { width: 1200px; height: 800px; overflow: hidden; }
  body { background: var(--backdrop); position: relative; font-family: "Lato", sans-serif; }

  .label {
    position: absolute;
    top: 290px;
    width: 220px;
    height: 440px;
    background: var(--label-black);
    color: var(--ivory);
    text-align: center;
    border-radius: 6px;
  }
  .label--back { left: 140px; }
  .label--oil { left: 500px; }
  .label--mist { left: 784px; }

  .label > * { position: absolute; left: 0; right: 0; }

  .brand-name {
    top: 32px;
    font-family: "Josefin Sans", sans-serif;
    font-weight: 600;
    font-size: 15px;
    letter-spacing: 2.5px;
  }
  .brand-pattern {
    top: 72px; left: 52px; right: 52px; height: 54px;
    border-radius: 4px;
  }
  .brand-pattern--oil {
    background: radial-gradient(ellipse at center, var(--amber-deep) 0%, var(--sage) 45%, rgba(142,148,132,0.55) 75%, rgba(12,12,12,0) 100%);
  }
  .brand-pattern--mist {
    background: radial-gradient(ellipse at center, var(--crimson) 0%, #8e8a84 45%, rgba(142,138,132,0.55) 75%, rgba(12,12,12,0) 100%);
  }
  .verse {
    top: 144px;
    font-family: "Dancing Script", cursive;
    font-size: 10px;
    line-height: 13px;
    color: var(--verse);
  }
  .product-name {
    top: 306px;
    font-family: "Oswald", sans-serif;
    font-weight: 600;
    font-size: 17px;
    letter-spacing: 0.5px;
  }
  .product-name--oil { color: var(--amber); }
  .product-name--mist { color: var(--crimson); }
  .product-claim {
    top: 352px;
    font-size: 9.5px;
    line-height: 14px;
  }
  .border-pattern {
    top: 378px; left: 26px; right: 26px; height: 26px;
    border-radius: 3px;
    background: linear-gradient(90deg,
      rgba(200,196,186,0.35), var(--kente-red) 18%, rgba(200,196,186,0.55) 34%,
      var(--kente-green) 50%, rgba(200,196,186,0.55) 66%, var(--kente-gold) 82%, rgba(200,196,186,0.35));
    opacity: 0.85;
  }

  .ingredients, .directions, .caution {
    left: 16px; right: 16px;
    font-size: 8.5px;
    line-height: 11px;
    color: var(--muted);
    text-align: center;
  }
  .ingredients { top: 170px; }
  .directions { top: 220px; }
  .caution { top: 251px; }
  .back-pattern {
    top: 272px; left: 50px; right: 50px; height: 52px;
    border-radius: 4px;
    background: radial-gradient(ellipse at center, #4a4a4a 0%, var(--pattern-grey) 40%, rgba(40,40,40,0.6) 75%, rgba(12,12,12,0) 100%);
  }
  .producer {
    top: 336px;
    font-size: 9px;
    line-height: 12px;
    color: var(--ivory);
  }
  .producer-title { font-style: italic; }
  .producer-name { font-size: 11px; letter-spacing: 0.5px; }
  .label--back .border-pattern { top: 388px; height: 20px; }
</style>
</head>
<body>

  <section class="label label--back">
    <p class="ingredients">Ingredients: Jamaican Black Castor Oil,<br>Argan Oil, Avocado Oil, Sweet Almond Oil,<br>Vitamin E Oil, Tea Tree Oil, Jojoba Oil,<br>Coconut Oil.</p>
    <p class="directions">How to Use: Hot oil treatment, directly<br>on scalp or hair, seal in moisture.</p>
    <p class="caution">FOR EXTERNAL USE ONLY.</p>
    <div class="back-pattern" role="img" aria-label="Faint grey geometric African pattern motif"></div>
    <div class="producer">
      <p class="producer-title">PRODUCED BY:</p>
      <p class="producer-name">AMBER MEADOW</p>
      <p>Picstream: AmberMeadow33</p>
      <p>Friendwall: fw.me/AmberMeadow33</p>
    </div>
    <div class="border-pattern" role="img" aria-label="Geometric diamond border pattern in ivory, red, green and gold"></div>
  </section>

  <section class="label label--oil">
    <h1 class="brand-name">AMBER MEADOW</h1>
    <div class="brand-pattern brand-pattern--oil" role="img" aria-label="Symmetric geometric African pattern motif in sage, ivory and amber"></div>
    <p class="verse">"But if a woman have long hair,<br>it is a glory to her<br>for her hair is given her for a covering"</p>
    <h2 class="product-name product-name--oil">360 HAIR OIL</h2>
    <p class="product-claim">100% Natural Oils<br>8oz</p>
    <div class="border-pattern" role="img" aria-label="Geometric diamond border pattern in ivory, red, green and gold"></div>
  </section>

  <section class="label label--mist">
    <h1 class="brand-name">AMBER MEADOW</h1>
    <div class="brand-pattern brand-pattern--mist" role="img" aria-label="Symmetric geometric African pattern motif in grey, ivory and crimson"></div>
    <p class="verse">"But if a woman have long hair,<br>it is a glory to her<br>for her hair is given her for a covering"</p>
    <h2 class="product-name product-name--mist">LOCS HAIR MIST</h2>
    <p class="product-claim">100% Natural Oils<br>8oz</p>
    <div class="border-pattern" role="img" aria-label="Geometric diamond border pattern in ivory, red, green and gold"></div>
  </section>

</body>
</html>
```